Business Card Design for Occupational Medicine Start Up Company

We need to design a professional business card. We are a healthcare company providing occupational medicine services to blue collar industries. We are professional, efficient and high quality service providers.

Target Market(s)

Blue Collar Industry: Shipbuilding, Ports, Trucking Companies; The Executives and Safety Officers for these companies

Industry/Entity Type

Healthcare

Contact Information for Business Card

Logo, Name, Title, Email, Phone

Other font styles liked:
• Please match our Brand Guide

Requirements
Must have
• Our Company Colors and Logo

```html
<!DOCTYPE html>
<html lang="en">
<head>
<meta charset="utf-8">
<title>Harborline Care – Business Card</title>
<link href="https://fonts.googleapis.com/css2?family=Arimo:wght@400;700&display=swap" rel="stylesheet">
<style>
  :root {
    --navy: #2b3580;
    --navy-deep: #283582;
    --sky: #29a8e0;
    --amber: #f6ac3b;
    --white: #ffffff;
    --backdrop: #9b9b9b;
    --mark-tint: #5868e0;
  }
  * { margin: 0; padding: 0; box-sizing: border-box; }
  html, body { width: 1133px; height: 1200px; overflow: hidden; }
  body {
    background: var(--backdrop);
    font-family: "Arimo", Arial, sans-serif;
    position: relative;
  }
  .card {
    position: absolute;
    left: 198px;
    width: 724px;
    height: 412px;
    overflow: hidden;
  }
  .card--front { top: 144px; background: var(--white); }
  .card--back { top: 640px; background: var(--navy-deep); }

  .front-shape { position: absolute; inset: 0; }

  .contact { position: absolute; left: 41px; top: 100px; color: var(--white); }
  .contact__name { color: var(--sky); font-weight: 700; font-size: 24px; line-height: 1; }
  .contact__title { color: var(--amber); font-size: 17px; margin-top: 6px; }
  .contact__address { font-size: 17px; line-height: 20px; margin-top: 10px; }
  .contact__list { list-style: none; margin-top: 10px; font-size: 17px; line-height: 20.5px; }
  .contact__list li { display: flex; align-items: center; gap: 9px; }
  .contact__list svg { width: 12px; height: 12px; flex: none; fill: var(--sky); }

  .wordmark {
    position: absolute;
    left: 403px; width: 290px; top: 135px;
    display: flex; flex-direction: column; align-items: center; gap: 18px;
  }
  .wordmark__dot { width: 56px; height: 56px; border-radius: 50%; background: var(--navy); }
  .wordmark__name {
    color: var(--navy); font-weight: 700; font-size: 28px;
    letter-spacing: 1px; text-transform: uppercase; white-space: nowrap;
  }

  .back-mark {
    position: absolute; left: 0; right: 0; top: 78px;
    display: flex; flex-direction: column; align-items: center; gap: 22px;
  }
  .back-mark__dot { width: 110px; height: 110px; border-radius: 50%; background: var(--mark-tint); }
  .back-mark__name { color: var(--mark-tint); font-weight: 700; font-size: 40px; letter-spacing: 1px; }

  .back-web {
    position: absolute; left: 0; right: 0; top: 348px;
    text-align: center; color: var(--white);
    font-size: 16px; letter-spacing: 4px;
  }
  .back-web strong { font-weight: 700; }
</style>
</head>
<body>
  <section class="card card--front">
    <svg class="front-shape" viewBox="0 0 724 412" preserveAspectRatio="none">
      <path d="M0 0 H259 C290 8 304 35 314 70 L408 412 H0 Z" fill="var(--amber)"/>
      <path d="M0 0 H251 C282 8 296 35 306 70 L400 412 H0 Z" fill="var(--white)"/>
      <path d="M0 0 H248 C279 8 293 35 303 70 L397 412 H0 Z" fill="var(--sky)"/>
      <path d="M0 0 H241 C272 8 286 35 296 70 L390 412 H0 Z" fill="var(--navy)"/>
    </svg>

    <div class="contact">
      <p class="contact__name">Daniel Reyes</p>
      <p class="contact__title">President</p>
      <p class="contact__address">412 Harbor View Road<br>Bayfield, Oregon 97411</p>
      <ul class="contact__list">
        <li><svg viewBox="0 0 12 12"><path d="M2 1 L4 1 L5 4 L3.6 5 C4.3 6.6 5.4 7.7 7 8.4 L8 7 L11 8 L11 10 C11 10.6 10.6 11 10 11 C5 11 1 7 1 2 C1 1.4 1.4 1 2 1Z"/></svg>555-204-7718</li>
        <li><svg viewBox="0 0 12 12"><path d="M3 0 H9 V12 H3 Z M4 1.5 V9.5 H8 V1.5 Z"/></svg>555-309-6142</li>
        <li><svg viewBox="0 0 12 12"><path d="M3 0 H9 V4 H3 Z M0 5 H12 V10 H10 V8 H2 V10 H0 Z M2 9 H10 V12 H2 Z"/></svg>555-417-2093</li>
        <li><svg viewBox="0 0 12 12"><path d="M0 2 H12 V10 H0 Z M1 3 L6 7 L11 3 Z" fill-rule="evenodd"/></svg>hello@harborlinecare.com</li>
        <li><svg viewBox="0 0 12 12"><circle cx="6" cy="6" r="6"/></svg>www.harborlinecare.com</li>
      </ul>
    </div>

    <div class="wordmark">
      <span class="wordmark__dot"></span>
      <span class="wordmark__name">Harborline Care</span>
    </div>
  </section>

  <section class="card card--back">
    <div class="back-mark">
      <span class="back-mark__dot"></span>
      <span class="back-mark__name">Harborline Care</span>
    </div>
    <p class="back-web">www.<strong>HarborlineCare</strong>.com</p>
  </section>
</body>
</html>
```